Vegan Alfredo Sauce Label Design for Brambleway Pantry Co

We are a food co. committed to making vegan food more accessible to people who want to eat healthier. Our first line of product is vegan Alfredo sauce.
We have 3 flavors:
- Garlic
- Pesto
- Lemony Artichoke
The current project is the design for the first flavor: garlic. However, we would like a template that would translate well to other flavors, so they look like a family of products.
These will be in standard 16 oz jars. The whole label will be approx 6cm x 24cm, but the front visual space is approx 6cm x 10cm. The rest will be nutritional labeling and copy about the company.
We also need a stamp or font- based logo that says Brambleway Pantry Co. (or lower case: brambleway pantry co.), the name of the company.
The picture (attached) of Plantbased Nacho Dip is the closest to what we are going for. Because the sauce is creamy white, a colorful background with off-white font will be best.
We currently have a website, although we are doing a brand over-haul (hence, this posting) www.bramblewaypantryco.example. If the designer is a good fit, we have several more projects, in line.
Other brands we love: Tidewell Grocers, Marlow Ridge Provisions, Pulp Poured Daily.
The final brand should communicate hip, natural and health.
And personally, I love design that is clever and somehow makes me smile.
Target Market(s)
Vegans, vegetarians, and people with common food allergies - all ages.
Young, hip families.
Industry/Entity Type
It Company
Requirements
Must have
- Copy:
Vegan Alfredo or Vegan Alfredo Sauce
Garlic
Brambleway Pantry or Brambleway Pantry Co
16 oz
Nice to have
- May include copy:
Gluten-Free Soy-Free Nut-Free
Should not have
- Neon colors

```html
<!DOCTYPE html>
<html lang="en">
<head>
<meta charset="utf-8">
<title>Brambleway Pantry Co — Vegan Alfredo Sauce Labels, Option 2</title>
<link rel="stylesheet" href="https://fonts.googleapis.com/css2?family=Oswald:wght@500&family=Roboto+Condensed:wght@400;500&family=Cinzel:wght@400&display=swap">
<style>
  :root {
    --page-bg: #ffffff;
    --heading-ink: #333333;
    --cream: #eef1c6;
    --band-black: #1c1b1b;
    --lemony-gold: #d8c060;
    --garlic-purple: #8c1a7f;
    --garlic-purple-deep: #6f1364;
    --artichoke-green: #4e8a27;
    --artichoke-green-deep: #3f7320;
    --pesto-green: #7aa32d;
    --pesto-green-deep: #66902a;
  }
  * { box-sizing: border-box; margin: 0; padding: 0; }
  html, body {
    width: 1200px;
    height: 900px;
    overflow: hidden;
    background: var(--page-bg);
  }
  .board {
    position: relative;
    width: 1200px;
    height: 900px;
  }
  .option-title {
    position: absolute;
    left: 38px;
    top: 24px;
    font-family: "Cinzel", serif;
    font-weight: 400;
    font-size: 22px;
    letter-spacing: 5px;
    color: var(--heading-ink);
  }
  .label {
    position: absolute;
    top: 298px;
    width: 244px;
    height: 246px;
    overflow: hidden;
    color: var(--cream);
    text-align: center;
  }
  .label--garlic { left: 198px; }
  .label--artichoke { left: 479px; }
  .label--pesto { left: 759px; }

  .label__art {
    position: absolute;
    inset: 0;
  }
  .label--garlic .label__art {
    background: linear-gradient(115deg, var(--garlic-purple) 0%, var(--garlic-purple-deep) 45%, var(--garlic-purple) 100%);
  }
  .label--artichoke .label__art {
    background: linear-gradient(115deg, var(--artichoke-green) 0%, var(--artichoke-green) 50%, var(--artichoke-green-deep) 100%);
  }
  .label--pesto .label__art {
    background: linear-gradient(115deg, var(--pesto-green-deep) 0%, var(--pesto-green) 45%, var(--pesto-green-deep) 100%);
  }

  .label__content {
    position: relative;
    display: flex;
    flex-direction: column;
    align-items: center;
    height: 100%;
  }
  .brand-mark {
    margin-top: 24px;
    display: flex;
    align-items: center;
    gap: 4px;
    font-family: "Roboto Condensed", sans-serif;
    font-weight: 400;
    font-size: 12.5px;
    color: #ffffff;
  }
  .brand-mark__dot {
    width: 6px;
    height: 6px;
    border-radius: 50%;
    background: #ffffff;
  }
  .flavor-note {
    margin-top: 14px;
    height: 16px;
    font-family: "Roboto Condensed", sans-serif;
    font-weight: 500;
    font-size: 14px;
    letter-spacing: 1.5px;
    color: var(--lemony-gold);
  }
  .flavor-name {
    font-family: "Oswald", sans-serif;
    font-weight: 500;
    line-height: 1;
    white-space: nowrap;
    letter-spacing: -0.5px;
    transform-origin: center top;
  }
  .flavor-name--short {
    margin-top: 10px;
    font-size: 82px;
    transform: scaleY(1.05);
  }
  .flavor-name--long {
    margin-top: 2px;
    font-size: 64px;
    letter-spacing: -1.5px;
    transform: scale(0.84, 1.35);
  }
  .product-band {
    position: absolute;
    top: 157px;
    left: 50%;
    transform: translateX(-50%);
    padding: 1px 7px 0;
    background: var(--band-black);
    font-family: "Roboto Condensed", sans-serif;
    font-weight: 500;
    font-size: 15px;
    letter-spacing: 0.6px;
    white-space: nowrap;
    color: #ffffff;
  }
  .free-from {
    position: absolute;
    top: 192px;
    left: 0;
    right: 0;
    font-family: "Roboto Condensed", sans-serif;
    font-size: 9px;
    letter-spacing: 0.3px;
    white-space: nowrap;
    color: #ffffff;
  }
  .net-weight {
    position: absolute;
    top: 216px;
    left: 0;
    right: 0;
    font-family: "Roboto Condensed", sans-serif;
    font-size: 12px;
    color: #ffffff;
  }
</style>
</head>
<body>
<main class="board">
  <h1 class="option-title">OPTION 2</h1>

  <section class="label label--garlic">
    <div class="label__art" role="img" aria-label="Loose brush-style illustration of a garlic bulb in deep purple tones"></div>
    <div class="label__content">
      <p class="brand-mark"><span class="brand-mark__dot"></span>brambleway pantry co</p>
      <h2 class="flavor-name flavor-name--short">GARLIC</h2>
      <p class="product-band">VEGAN ALFREDO SAUCE</p>
      <p class="free-from">GLUTEN-FREE • SOY-FREE • NUT-FREE</p>
      <p class="net-weight">16oz</p>
    </div>
  </section>

  <section class="label label--artichoke">
    <div class="label__art" role="img" aria-label="Loose brush-style illustration of an artichoke in darker green tones"></div>
    <div class="label__content">
      <p class="brand-mark"><span class="brand-mark__dot"></span>brambleway pantry co</p>
      <p class="flavor-note">LEMONY</p>
      <h2 class="flavor-name flavor-name--long">ARTICHOKE</h2>
      <p class="product-band">VEGAN ALFREDO SAUCE</p>
      <p class="free-from">GLUTEN-FREE • SOY-FREE • NUT-FREE</p>
      <p class="net-weight">16oz</p>
    </div>
  </section>

  <section class="label label--pesto">
    <div class="label__art" role="img" aria-label="Loose brush-style illustration of basil leaves in olive green tones"></div>
    <div class="label__content">
      <p class="brand-mark"><span class="brand-mark__dot"></span>brambleway pantry co</p>
      <h2 class="flavor-name flavor-name--short">PESTO</h2>
      <p class="product-band">VEGAN ALFREDO SAUCE</p>
      <p class="free-from">GLUTEN-FREE • SOY-FREE • NUT-FREE</p>
      <p class="net-weight">16oz</p>
    </div>
  </section>
</main>
</body>
</html>
```